Electrical Contractor Brochure, Folder and Letter Head

Barrowfield Electrical Ltd. is an Edmonton based electrical contractor focusing on commercial and industrial electrical services. Our target market is manufacturing facilities, warehouses and commercial buildings.

We want to seem larger than we are with service vehicles and electricians ready to dispatch to service calls and new installations. Our key color is the blue in the logo. The BFE logo is well branded in Edmonton and should be on the brochure.

We are looking for a tri-fold brochure, full-page brochure with folder sleeves and a letter head.
Updates

Please ignore the second page of copy.  I only want the electrical content in the brochure.  This is my mistake.  Please use only the first page of copy.

Industry/Entity Type

Electrical

Requirements
Must have
• Many background pics of the services, electricians and projects. I like the faded BFE logo in the background of the letterhead! Folder Size A4
Nice to have
• Try the pic named Cover Pic1 to on the front of the brochure.
Should not have
• DO NOT USE ANY WEBSITE CONTENT. THIS IS NOT OUR BUSINESS. PLEASE USE ONLY CONTENT AND COLOR FROM THE ATTACHED FILES!!

```html
<!DOCTYPE html>
<html lang="en">
<head>
<meta charset="utf-8">
<title>Barrowfield Electrical Ltd. – Tri-fold Brochure</title>
<link rel="stylesheet" href="https://fonts.googleapis.com/css2?family=Open+Sans:ital,wght@0,400;0,600;0,700;1,700&display=swap">
<style>
  :root {
    --page-bg: #e4e4e6;
    --panel-dark: #252526;
    --panel-darker: #1b1b1c;
    --band-light: #d9d9da;
    --band-mid: #8c8c8e;
    --brand-blue: #1f4fa8;
    --accent-blue: #2f9be0;
    --violet-top: #3d63b8;
    --violet-bottom: #241a63;
    --text-light: #f2f2f2;
    --text-soft: #d6d8ea;
    --photo-shop: #8a8f96;
    --photo-panel: #5c6a80;
  }
  * { box-sizing: border-box; margin: 0; padding: 0; }
  html, body {
    width: 1200px; height: 932px; overflow: hidden;
    background: var(--page-bg);
    font-family: "Open Sans", Arial, sans-serif;
  }
  .brochure {
    position: absolute; left: 60px; top: 116px;
    width: 1080px; height: 700px;
    display: flex;
    box-shadow: 0 18px 40px rgba(0,0,0,.25);
  }
  .panel { position: relative; width: 360px; height: 700px; overflow: hidden; }

  /* Left panel */
  .panel--intro { background: var(--panel-dark); }
  .intro__header {
    height: 130px;
    background: linear-gradient(180deg, var(--band-light), var(--band-mid));
    display: flex; align-items: center; justify-content: center; gap: 10px;
  }
  .brand-mark { width: 22px; height: 22px; background: var(--brand-blue); }
  .brand-name { color: var(--brand-blue); font-weight: 700; font-size: 21px; }
  .section-tab {
    position: absolute; left: 20px; top: 124px;
    width: 230px; height: 40px;
    background: linear-gradient(180deg, #4a4a4c, #2b2b2c);
    border-radius: 3px;
    box-shadow: 0 4px 8px rgba(0,0,0,.45);
    display: flex; align-items: center; padding-left: 22px;
    color: var(--accent-blue); font-style: italic; font-weight: 700; font-size: 20px;
  }
  .intro__body { position: absolute; left: 30px; top: 190px; right: 26px; color: var(--text-light); }
  .lead { font-size: 12.5px; line-height: 1.45; margin-bottom: 18px; }
  .service-list { list-style: none; font-size: 13px; line-height: 1.4; }
  .intro__footer { position: absolute; left: 0; bottom: 0; width: 360px; height: 150px; }

  /* Middle panel */
  .panel--business { background: linear-gradient(180deg, var(--violet-top), var(--violet-bottom)); }
  .photo { position: absolute; }
  .photo--workshop {
    left: 0; top: 180px; width: 360px; height: 190px;
    background: linear-gradient(135deg, #c9ccd0 0%, var(--photo-shop) 45%, #3e4a72 100%);
  }
  .business__body { position: absolute; left: 26px; top: 395px; right: 22px; color: var(--text-soft); }
  .business__title { color: var(--accent-blue); font-weight: 700; font-size: 25px; margin-bottom: 10px; }

  /* Right panel */
  .panel--services { background: var(--panel-dark); }
  .services__art { position: absolute; inset: 0; }
  .photo--electrician {
    left: 24px; top: 140px; width: 300px; height: 200px;
    background: linear-gradient(120deg, #2f3a4a 0%, var(--photo-panel) 50%, #c7d3e2 100%);
  }
  .services__body { position: absolute; left: 40px; top: 380px; color: var(--text-light); }
</style>
</head>
<body>
<main class="brochure">

  <section class="panel panel--intro">
    <header class="intro__header">
      <span class="brand-mark"></span>
      <span class="brand-name">Barrowfield Electrical</span>
    </header>
    <h2 class="section-tab">What We Do?</h2>
    <div class="intro__body">
      <p class="lead">Barrowfield Machine Services Ltd. provides services that are vital to cost effective production and reducing costly down time with CNC and Conventional machines, Band Saws and Production equipment.</p>
      <ul class="service-list">
        <li>Mechanical and Electrical Troubleshooting</li>
        <li>PLC Troubleshooting</li>
        <li>Collision Recovery</li>
        <li>Machine Installations</li>
        <li>Machine Decommissioning</li>
        <li>Servo Diagnostics</li>
        <li>Preventive Maintenance Plans</li>
        <li>Inspections</li>
        <li>Parts Replacement</li>
        <li>Lubrication Oil Supply</li>
        <li>Parts Supply</li>
      </ul>
    </div>
    <svg class="intro__footer" viewBox="0 0 360 150" aria-hidden="true">
      <path d="M0 20 Q180 0 360 30 L360 150 L0 150 Z" fill="var(--panel-darker)"/>
    </svg>
  </section>

  <section class="panel panel--business">
    <div class="photo photo--workshop" role="img" aria-label="Photo of a machine shop with a technician servicing a lathe"></div>
    <div class="business__body">
      <h2 class="business__title">Open for Business</h2>
      <p class="lead">Barrowfield Machine Services Ltd. provides services that are vital to cost effective production and reducing costly down time with CNC and Conventional machines, Band Saws and Production equipment.</p>
      <ul class="service-list">
        <li>Mechanical and Electrical Troubleshooting</li>
        <li>PLC Troubleshooting</li>
        <li>Collision Recovery</li>
        <li>Machine Installations</li>
        <li>Machine Decommissioning</li>
        <li>Servo Diagnostics</li>
      </ul>
    </div>
  </section>

  <section class="panel panel--services">
    <svg class="services__art" viewBox="0 0 360 700" aria-hidden="true">
      <path d="M0 0 H300 Q200 50 0 60 Z" fill="var(--panel-darker)"/>
      <path d="M0 610 Q150 600 230 640 L200 700 L0 700 Z" fill="#2f2f31"/>
      <path d="M270 0 C360 160 380 520 200 700 L360 700 L360 0 Z" fill="var(--brand-blue)"/>
      <path d="M250 0 C345 160 365 520 185 700" fill="none" stroke="var(--accent-blue)" stroke-width="5"/>
      <path d="M300 0 C380 200 380 520 260 700 L360 700 L360 0 Z" fill="var(--violet-bottom)" opacity=".55"/>
    </svg>
    <div class="photo photo--electrician" role="img" aria-label="Photo of an electrician in a hard hat wiring a control panel"></div>
    <div class="services__body">
      <ul class="service-list">
        <li>Machine Decommissioning</li>
        <li>Servo Diagnostics</li>
        <li>Preventive Maintenance Plans</li>
        <li>Inspections</li>
        <li>Parts Replacement</li>
        <li>Lubrication Oil Supply</li>
        <li>Parts Supply</li>
      </ul>
    </div>
  </section>

</main>
</body>
</html>
```